Kem7Dex Letterhead

Need a new letterhead for my law firm.
IDENTIFYING INFORMATION BELOW:
Ansel T Brightwater III
Attorney at Law
Address: 4832 Tillbury Rd, Ste 250, Dallas, TX 75204
Phone: 866-402-7183
Fax: 469-583-0271
Email: kem@kem7dex.example
Website: www.kem7dex.example

Colors
0054AA
0677BA
7BADD7
CADEEF
E8F1F8

Requirements
Must have
• Logo needs to be on the letterhead, along with identifying information which is included in the project description.

```html
<!DOCTYPE html>
<html lang="en">
<head>
<meta charset="utf-8">
<title>Kem7Dex Letterhead</title>
<link rel="stylesheet" href="https://fonts.googleapis.com/css2?family=Poppins:wght@300;400;500;600;800&display=swap">
<style>
  :root {
    --backdrop: #e2e2e2;
    --paper: #ffffff;
    --ink: #111111;
    --body-ink: #2b2b2b;
    --muted: #3a3a3a;
    --brand-light: #16a3dc;
    --brand-dark: #04569a;
    --icon: #0677ba;
    --sig-fill: #e8f1f8;
  }
  * { box-sizing: border-box; margin: 0; padding: 0; }
  html, body { width: 1200px; height: 1200px; overflow: hidden; }
  body {
    background: var(--backdrop);
    font-family: "Poppins", Arial, sans-serif;
    color: var(--body-ink);
  }
  .letterhead {
    position: absolute;
    left: 204px; top: 40px;
    width: 792px; height: 1120px;
    background: var(--paper);
  }
  .brand {
    position: absolute;
    left: 0; right: 0; top: 62px;
    text-align: center;
  }
  .brand-name {
    font-weight: 800;
    font-size: 54px;
    line-height: 1;
    letter-spacing: 1px;
    color: var(--ink);
  }
  .brand-tagline {
    margin-top: 6px;
    font-weight: 300;
    font-size: 22px;
    letter-spacing: 4px;
    color: var(--ink);
  }
  .recipient, .salutation, .letter-body {
    position: absolute;
    left: 75px;
    font-size: 13.4px;
    line-height: 21.3px;
  }
  .recipient { top: 224px; }
  .salutation { top: 380px; }
  .letter-body { top: 422px; width: 641px; text-align: justify; }
  .letter-body p { margin: 0; }
  .signature {
    position: absolute;
    left: 70px; top: 805px;
    width: 300px; height: 56px;
    background: linear-gradient(90deg, var(--sig-fill), #f5f8fb);
    border-radius: 4px;
  }
  .signer { position: absolute; left: 70px; top: 866px; }
  .signer-name {
    font-weight: 600;
    font-size: 13.4px;
    letter-spacing: 1.4px;
    color: var(--ink);
  }
  .signer-title {
    font-size: 9.6px;
    letter-spacing: 1.4px;
    color: var(--muted);
    margin-top: 1px;
  }
  .contact { position: absolute; left: 70px; top: 1013px; color: var(--ink); }
  .contact-address { font-weight: 500; font-size: 14.6px; margin-bottom: 4px; }
  .contact-row { display: flex; gap: 12px; font-size: 12.6px; line-height: 18px; }
  .contact-item { display: flex; align-items: center; gap: 3px; }
  .contact-item svg { width: 10px; height: 10px; fill: var(--icon); }
  .footer-band { position: absolute; left: 0; bottom: 0; width: 792px; height: 23px; display: block; }
</style>
</head>
<body>
  <main class="letterhead">
    <header class="brand">
      <div class="brand-name">KEM7DEX</div>
      <div class="brand-tagline">RIGHT BY YOUR SIDE</div>
    </header>

    <address class="recipient" style="font-style:normal">
      Mr. John Doe<br>
      President<br>
      Strategy Accountants<br>
      111 Street Name,<br>
      City State, 12345
    </address>

    <p class="salutation">Dear</p>

    <section class="letter-body">
      <p>Lorem ipsum dolor sit amet, consectetur adipiscing elit. Aenean ut ipsum eget massa hendrerit vestibulum vel in velit. Donec pretium neque velit.</p>
      <p>Aliquam porta lectus nec mauris ornare venenatis. Vivamus non est turpis, et cursus sem. Mauris vehicula erat in diam auctor at bibendum nisl lacinia.</p>
      <p>Morbi imperdiet neque vehicula nunc convallis gravida. Vestibulum iaculis pretium placerat. Integer consequat, est sit amet facilisis eleifend, nibh nibh varius orci, eget dapibus arcu dui non purus. Pellentesque in magna mauris. Duis enim sapien, dictum vitae condimentum a, pulvinar vel lacus. Mauris et molestie nibh. Vestibulum vitae nulla at metus elementum porta sit amet interdum elit. Nulla sollicitudin neque eu nulla volutpat congue.</p>
      <p>Etiam pellentesque, velit id dapibus fermentum, turpis sapien ornare dui, ac tincidunt ligula odio congue purus. Nunc sed ante dui, in porta lectus. Cras nec sem lorem. In hac habitasse platea dictumst. Maecenas id diam quis dui porta tristique. Sed id egestas felis. Donec ullamcorper mattis posuere. Phasellus fermentum eleifend tortor vel dapibus. Vestibulum ante ipsum.</p>
    </section>

    <div class="signature" role="img" aria-label="Handwritten signature of Ansel T Brightwater III"></div>

    <div class="signer">
      <div class="signer-name">ANSEL T BRIGHTWATER III</div>
      <div class="signer-title">ATTORNEY AT LAW</div>
    </div>

    <footer class="contact">
      <div class="contact-address">4832 Tillbury Rd, Ste 250, Dallas, TX 75204</div>
      <div class="contact-row">
        <span class="contact-item">
          <svg viewBox="0 0 10 10" aria-hidden="true"><path d="M2.2 0.6l1.6 1.8-0.9 1.1c0.6 1.3 1.5 2.2 2.7 2.8l1.1-0.9 1.8 1.6-1 1.6C4.6 8.4 1.4 5.2 0.6 1.6z"/></svg>
          866-402-7183
        </span>
        <span class="contact-item">
          <svg viewBox="0 0 10 10" aria-hidden="true"><rect x="2.5" y="0.5" width="5" height="3"/><rect x="0.8" y="3.8" width="8.4" height="4" rx="0.8"/><rect x="2.5" y="7" width="5" height="2.5"/></svg>
          469-583-0271
        </span>
      </div>
      <div class="contact-row">
        <span class="contact-item">
          <svg viewBox="0 0 10 10" aria-hidden="true"><path d="M0.5 2h9v6.5h-9z M1.2 2.6L5 5.6 8.8 2.6" stroke="#fff" stroke-width="0.7"/></svg>
          kem@kem7dex.example
        </span>
        <span class="contact-item">
          <svg viewBox="0 0 10 10" aria-hidden="true"><circle cx="5" cy="5" r="4.4" fill="none" stroke="var(--icon)" stroke-width="0.9"/><ellipse cx="5" cy="5" rx="1.9" ry="4.4" fill="none" stroke="var(--icon)" stroke-width="0.8"/><path d="M0.6 5h8.8M1.3 3h7.4M1.3 7h7.4" stroke="var(--icon)" stroke-width="0.7"/></svg>
          www.kem7dex.example
        </span>
      </div>
    </footer>

    <svg class="footer-band" viewBox="0 0 792 23" preserveAspectRatio="none" aria-hidden="true">
      <polygon points="0,0 271,0 259,23 0,23" fill="var(--brand-light)"/>
      <polygon points="275,0 792,0 792,23 263,23" fill="var(--brand-dark)"/>
    </svg>
  </main>
</body>
</html>
```